Business Card - Professional Minimalist - Double sided

We appreciate minimalist logo/web/collateral designs that allow design to tell a story. We want to relay a professional image/approach but throwing in a splash of modern when we’re able so long as it’s not distracting. Think 75% classic corporate, 25% modern. Open to black or white design, not sure which might look the best.

Target Market(s)

Senior executives or related government affairs contacts within the agriculture, energy, and defense industries (i.e., potential clients) but located outside of Washington, DC. Most potential clients based in DC with be familiar with both of us and our shared history.

Industry/Entity Type

Consulting

Contact Information for Business Card

Name: Daniel R. Whitlock
Title: Co-Founder & Partner
Address: 418 Bramblewood Ave. SE | Suite 2716 | Washington, D.C. 20019
Phone: (202) 555-0187
Email: Daniel@HollerbyWhitlock.com

Font styles to use
Serif

Colors

Designer to choose only greyscale colors for use in the design.

Requirements
Must have
• Name: Daniel R. Whitlock
Phone: (202) 555-0187

```html
<!DOCTYPE html>
<html lang="en">
<head>
<meta charset="utf-8">
<title>Hollerby Whitlock Group – Business Card</title>
<link href="https://fonts.googleapis.com/css2?family=Tinos:wght@400;700&display=swap" rel="stylesheet">
<style>
  :root {
    --backdrop: #e6e9e9;
    --card-black: #1f1d1e;
    --card-white: #ffffff;
    --band-dark: #6a6a6a;
    --band-light: #a9a9a9;
    --ink-dark: #4a4a4a;
    --ink-silver: #bfbfbf;
    --ink-white: #ffffff;
    --icon-bg: #4d4d4d;
  }
  * { box-sizing: border-box; margin: 0; padding: 0; }
  html, body { width: 1200px; height: 800px; overflow: hidden; }
  body {
    background: var(--backdrop);
    font-family: "Tinos", "Times New Roman", serif;
    display: flex;
    align-items: center;
    justify-content: center;
    gap: 60px;
  }
  .card {
    width: 500px;
    height: 286px;
    position: relative;
    overflow: hidden;
    box-shadow: 0 6px 18px rgba(0,0,0,0.12);
  }

  /* Brand lockup */
  .brand {
    display: flex;
    align-items: center;
    gap: 12px;
  }
  .brand-mark {
    width: 26px;
    height: 26px;
    border: 2px solid currentColor;
  }
  .brand-name {
    font-size: 24px;
    font-weight: 400;
    letter-spacing: 0.08em;
    text-transform: uppercase;
  }

  /* Front */
  .card-front {
    background: var(--card-black);
    color: var(--ink-silver);
    display: flex;
    align-items: center;
    justify-content: center;
  }

  /* Back */
  .card-back { background: var(--card-white); }
  .card-back .brand-area {
    height: 168px;
    display: flex;
    align-items: center;
    justify-content: center;
    color: var(--ink-dark);
  }
  .band-primary {
    height: 50px;
    background: var(--band-dark);
    color: var(--ink-white);
    display: flex;
    justify-content: space-between;
    align-items: center;
    padding: 0 22px;
  }
  .person-name {
    font-weight: 700;
    font-size: 16px;
    letter-spacing: 0.04em;
    text-transform: uppercase;
    line-height: 1.1;
  }
  .person-title {
    font-size: 9.5px;
    letter-spacing: 0.06em;
    text-transform: uppercase;
  }
  .address {
    display: flex;
    align-items: center;
    gap: 8px;
    text-align: right;
    font-size: 10px;
    line-height: 1.35;
  }
  .band-divider { height: 3px; background: var(--card-white); }
  .band-secondary {
    height: 65px;
    background: var(--band-light);
    color: var(--ink-white);
    padding: 12px 22px;
    display: flex;
    flex-direction: column;
    gap: 6px;
    font-size: 11px;
  }
  .contact-line { display: flex; align-items: center; gap: 8px; }
  .icon {
    width: 14px;
    height: 14px;
    border-radius: 3px;
    background: var(--icon-bg);
    display: flex;
    align-items: center;
    justify-content: center;
    flex-shrink: 0;
  }
  .icon svg { width: 9px; height: 9px; fill: var(--ink-white); }
</style>
</head>
<body>

  <section class="card card-front" aria-label="Card front">
    <div class="brand">
      <span class="brand-mark"></span>
      <span class="brand-name">Hollerby Whitlock Group</span>
    </div>
  </section>

  <section class="card card-back" aria-label="Card back">
    <div class="brand-area">
      <div class="brand">
        <span class="brand-mark"></span>
        <span class="brand-name">Hollerby Whitlock Group</span>
      </div>
    </div>

    <div class="band-primary">
      <div class="person">
        <div class="person-name">Daniel R. Whitlock</div>
        <div class="person-title">Co-Founder &amp; Partner</div>
      </div>
      <div class="address">
        <div>418 Bramblewood Ave. SE<br>Suite 2716, Washington, D.C. 20019</div>
        <span class="icon">
          <svg viewBox="0 0 10 10"><path d="M5 0.5a3.2 3.2 0 0 0-3.2 3.2C1.8 6 5 9.5 5 9.5S8.2 6 8.2 3.7A3.2 3.2 0 0 0 5 0.5zm0 4.5a1.3 1.3 0 1 1 0-2.6 1.3 1.3 0 0 1 0 2.6z"/></svg>
        </span>
      </div>
    </div>

    <div class="band-divider"></div>

    <div class="band-secondary">
      <div class="contact-line">
        <span class="icon">
          <svg viewBox="0 0 10 10"><path d="M2.2 0.8l1.4 1.9-0.9 1.1c0.6 1.3 1.6 2.3 2.9 2.9l1.1-0.9 1.9 1.4-0.8 1.8C4.5 9 1 5.5 0.4 1.6z"/></svg>
        </span>
        <span>(202) 555-0187</span>
      </div>
      <div class="contact-line">
        <span class="icon">
          <svg viewBox="0 0 10 10"><path d="M0.5 2h9v6h-9z M0.9 2.4L5 5.6 9.1 2.4" stroke="#4d4d4d" stroke-width="0.6"/></svg>
        </span>
        <span>Daniel@HollerbyWhitlock.com</span>
      </div>
    </div>
  </section>

</body>
</html>
```